QUORLANET - IT SERVICE PROVIDERS - TriFold Flyer

Looking for Exclusive Professional look TriFold Flyer (A4) to tell:
- what we do?
- Why choose us?
- Our Services
- Our Products
- Address and Contact Detail
From Designer:
=================
Look and Feel
Graphics - Icons - Shapes - Amazing Layouts - Exclusive Fonts.
All the content will be provided.
Please send your portfolio to check..
Reason: till now no one has send there designs - have to extend to get the designs...
If no one interested to give - then i need to ask a refund... thanx
Those who accepted my project - plz let me know your delivery dates...
and about content - plz mention the Titles which i have mentioned in Brief and put Lipsum text, i will replace them...
What i m looking is Awesome Layout and Design - Using Shapes / Graphics / Fonts... content u put lipsum content and more content you will get it from www.tenvoramix.com...
About services and other stuff.... thanx
Reason: not even 4 designers have submitted there design out of 13 acceptance.
Kindly send me the best design so as to give lots of projects...
Reason: Looking for more creative and unique design
Target Market(s)
Dubai and GCC
IT comsultants
IT Service Providers
Advertising Agencies
Software Development Cos.
Industry/Entity Type
It Professional
Look and feel

```html
<!DOCTYPE html>
<html lang="en">
<head>
<meta charset="utf-8">
<title>QUORLANET – IT Service Providers Tri-Fold Flyer</title>
<link rel="stylesheet" href="https://fonts.googleapis.com/css2?family=PT+Sans+Narrow:wght@400;700&family=Open+Sans:wght@300;400&display=swap">
<style>
  :root{
    --stage:#e8e8e8;
    --red:#e31d25;
    --red-deep:#b5121a;
    --wine:#7a0d14;
    --white:#ffffff;
    --ink:#2b2b2b;
    --frame:#9a9a9a;
    --copy-red:#d6242b;
  }
  *{box-sizing:border-box;margin:0;padding:0}
  html,body{width:1200px;height:659px;overflow:hidden;background:var(--stage)}
  .stage{position:relative;width:1200px;height:659px}
  .trifold{position:absolute;left:90px;top:40px;width:1020px;height:580px;display:flex;box-shadow:0 6px 18px rgba(0,0,0,.25)}
  .panel{position:relative;width:340px;height:580px;background:var(--red);overflow:hidden}
  .panel + .panel{border-left:1px solid rgba(0,0,0,.12)}

  .texture{position:absolute;inset:0;background:radial-gradient(circle at 50% 50%,rgba(90,0,0,.25),rgba(0,0,0,0) 70%)}

  /* Left panel – projects */
  .projects-title{position:absolute;left:22px;top:14px;font:300 28px/1 "Open Sans",sans-serif;color:var(--white);letter-spacing:-.5px}
  .projects-box{position:absolute;left:20px;top:50px;width:300px;height:486px;background:var(--white);border:1px solid var(--frame);outline:3px solid var(--white);padding:6px 8px;box-shadow:0 2px 6px rgba(0,0,0,.3)}
  .project{font:400 7.2px/1.18 "PT Sans Narrow",sans-serif;color:var(--copy-red);margin-bottom:3.1px}
  .project-name{font:400 13.5px/1 "PT Sans Narrow",sans-serif;color:var(--ink);margin-right:3px}

  /* Centre panel – brand */
  .burst{position:absolute;inset:0;background:
      radial-gradient(circle at 50% 50%,var(--wine) 0 52px,rgba(122,13,20,.55) 53px,rgba(122,13,20,.18) 150px,rgba(0,0,0,0) 240px)}
  .brand{position:absolute;left:0;right:0;top:268px;text-align:center;color:var(--white)}
  .brand-name{font:700 22px/1 "PT Sans Narrow",sans-serif;letter-spacing:.5px}
  .brand-tag{font:400 6px/1 "PT Sans Narrow",sans-serif;letter-spacing:2px;margin-top:3px}
  .brand-web{font:400 6px/1 "PT Sans Narrow",sans-serif;letter-spacing:1px;margin-top:2px}

  /* Right panel – about */
  .section-title{position:absolute;font:300 19px/1 "Open Sans",sans-serif;color:var(--white);letter-spacing:-.6px}
  .title-do{left:24px;top:106px}
  .title-why{right:22px;top:226px}
  .title-services{left:80px;top:340px}
  .info-box{position:absolute;left:30px;width:290px;background:var(--white);border:1px solid var(--frame);outline:3px solid var(--white);padding:8px 10px;font:400 8px/1.25 "PT Sans Narrow",sans-serif;color:var(--ink);box-shadow:0 2px 6px rgba(0,0,0,.3)}
  .box-do{top:145px;height:78px}
  .box-why{top:276px;height:62px}
  .box-services{top:392px;height:70px}

  .pointers{position:absolute;left:0;top:0;width:1020px;height:580px;pointer-events:none}
</style>
</head>
<body>
<div class="stage">
  <div class="trifold">
    <section class="panel panel-projects">
      <div class="texture" role="img" aria-label="Scattered thin dark red lines across the red background"></div>
      <h2 class="projects-title">PROJECTS</h2>
      <div class="projects-box">
        <p class="project"><span class="project-name">CRM</span>Customer Relationship Management will manage categories, products, customers, quotations, enquiry, purchase orders, invoice and reports.</p>
        <p class="project"><span class="project-name">Document Management</span>Add and manage users, document types and documents, search documents and view profile.</p>
        <p class="project"><span class="project-name">Accounting software</span>Covers inventory, purchase, sales, financial accounts, payable, receivable, trial balance, balance sheet and profit &amp; loss.</p>
        <p class="project"><span class="project-name">School management</span>Web based system with admin, student, teacher and parent modules, class details, attendance, library, timetable, exams and fees.</p>
        <p class="project"><span class="project-name">Hotel management</span>Admin and user modules to add hotels, rooms, menus and bookings, with room accessories, checkout and travel details.</p>
        <p class="project"><span class="project-name">e-commerce</span>Sellers list products, view stock and orders; buyers browse categories, shopping cart and checkout reports.</p>
        <p class="project"><span class="project-name">HRMS</span>Add company, client and employees, view tasks, timesheets, attendance, recruitment, performance and payroll.</p>
        <p class="project"><span class="project-name">Inventory software</span>Add customers, inventory, warehouse details, sales orders, purchase orders, invoices and delivery reports.</p>
        <p class="project"><span class="project-name">Sales and Invoicing</span>Admin, sales, customer and support modules with products, customers, leads, reports and email.</p>
        <p class="project"><span class="project-name">Car maintenance management</span>Dashboard, events, customers, equipment, invoices and reports with vehicle details and service history.</p>
        <p class="project"><span class="project-name">IT Customer service management</span>Add customer representatives, view customers and requests, send replies and track each response.</p>
        <p class="project"><span class="project-name">Clinic management</span>Admin, doctors registration, patient registration, appointments, reports, follow up.</p>
        <p class="project"><span class="project-name">Project management</span>Customer details, project details, project tracking, customer support, payment gateway.</p>
        <p class="project"><span class="project-name">Event management</span>Managing events, ticketing, payment gateway.</p>
        <p class="project"><span class="project-name">Job portal</span>Employer, candidates, admin control, search employer positions, search candidates.</p>
        <p class="project"><span class="project-name">Customer service</span>Admin search by ticket no, view, program, location and type; staff module with ticket search.</p>
        <p class="project"><span class="project-name">Social media membership</span>My blog, top blog, new blog, settings, profile, account, notifications, import feeds, links.</p>
      </div>
    </section>

    <section class="panel panel-brand">
      <div class="burst" role="img" aria-label="Explosion of thin dark lines radiating from a dark red star shape in the centre"></div>
      <div class="brand">
        <div class="brand-name">QUORLANET</div>
        <div class="brand-tag">IT SOLUTION PROVIDERS</div>
        <div class="brand-web">www.tenvoramix.com</div>
      </div>
    </section>

    <section class="panel panel-about">
      <div class="texture" role="img" aria-label="Scattered thin dark red lines across the red background"></div>
      <h3 class="section-title title-do">what we do?</h3>
      <p class="info-box box-do">Document management able to add and manage users, add and manage document types, add and manage documents and search documents. User will be able to view profile, add and manage document types, add and manage documents and search documents. Document management able to add and manage users, add and manage document types, add and manage documents and search documents. User will be able to view profile, add and manage document types, add and manage documents and search documents.</p>
      <h3 class="section-title title-why">Why choose us?</h3>
      <p class="info-box box-why">Document management able to add and manage users, add and manage document types, add and manage documents and search documents. User will be able to view profile, add and manage document types, add and manage documents and search documents. Document management able to add and manage users, add and manage document types, add and manage documents and search documents.</p>
      <h3 class="section-title title-services">Our Services</h3>
      <p class="info-box box-services">Document management able to add and manage users, add and manage document types, add and manage documents and search documents. User will be able to view profile, add and manage document types, add and manage documents and search documents. Document management able to add and manage users, add and manage document types, add and manage documents and search documents.</p>
    </section>

    <svg class="pointers" viewBox="0 0 1020 580" aria-hidden="true">
      <polygon points="318,150 318,190 452,258" fill="#ffffff"/>
      <polygon points="795,128 822,146 806,146" fill="#ffffff"/>
      <polygon points="848,136 872,146 860,146" fill="#ffffff"/>
      <polygon points="940,246 900,276 924,276" fill="#ffffff"/>
      <polygon points="836,358 870,392 884,392" fill="#ffffff"/>
    </svg>
  </div>
</div>
</body>
</html>
```